Business Card Design Project

Mabel's Tonics is a natural skincare business and we need a business card designed. The company focuses on natural products and will be launching with body scrubs and bath fizzies and our mission statement is: To deliver high quality natural beauty products at a good value. It's two cards - one design - the only information changing would be name and email address

Target Market(s)

Females ages 20-50

Industry/Entity Type

Business

Requirements
Must have
• Mabel's Tonics

Corinne Halvorsen-Pitt
T: 800-417-9368
E: Corinne@MabelsTonics.example
W: www.MabelsTonics.example

Ulrich Benedetti
T: 800-417-9368
E: Ulrich@MabelsTonics.example
W: www.MabelsTonics.example
Nice to have
• I'd like to use the colors or text found at www.mabelstonics.example but I'm open to suggestions since design isn't set in stone yet. I would also like to have the words .....a little bit of magic somewhere under the company name in a different type of font. I would like a design that feels clean and maybe a retro feel to it - front and back would be nice but not mandatory

```html
<!DOCTYPE html>
<html lang="en">
<head>
<meta charset="utf-8">
<title>Mabel's Tonics – Business Card</title>
<link rel="stylesheet" href="https://fonts.googleapis.com/css2?family=Montserrat:wght@700&family=Source+Sans+3:wght@400&display=swap">
<style>
  :root {
    --paper: #ffffff;
    --band-blue: #0092dd;
    --brand-purple: #7e2c83;
    --accent-grey: #8a8a8a;
    --text-light: #ffffff;
  }
  * { margin: 0; padding: 0; box-sizing: border-box; }
  html, body {
    width: 1200px;
    height: 628px;
    overflow: hidden;
    background: var(--paper);
  }
  .card {
    position: relative;
    width: 1200px;
    height: 628px;
    background: var(--paper);
    font-family: "Source Sans 3", "Myriad Pro", Arial, sans-serif;
  }
  .brand {
    position: absolute;
    top: 0;
    left: 0;
    width: 100%;
    height: 208px;
    display: flex;
    justify-content: center;
    align-items: flex-start;
    padding-top: 14px;
  }
  .brand-name {
    display: flex;
    align-items: center;
    gap: 14px;
    font-size: 64px;
    font-weight: 400;
    line-height: 1;
    color: var(--brand-purple);
    letter-spacing: 0.5px;
  }
  .brand-dot {
    width: 12px;
    height: 12px;
    border-radius: 50%;
    background: var(--accent-grey);
  }
  .contact-band {
    position: absolute;
    top: 208px;
    left: 0;
    width: 100%;
    height: 420px;
    background: var(--band-blue);
    color: var(--text-light);
    text-align: center;
  }
  .person-name {
    position: absolute;
    top: 36px;
    width: 100%;
    font-family: "Montserrat", "Century Gothic", Arial, sans-serif;
    font-weight: 700;
    font-size: 52px;
    line-height: 1;
    letter-spacing: 0.5px;
  }
  .contact-list {
    position: absolute;
    top: 188px;
    width: 100%;
    list-style: none;
    font-size: 46px;
    line-height: 66px;
  }
</style>
</head>
<body>
  <main class="card">
    <header class="brand">
      <div class="brand-name">Mabel's <span class="brand-dot" aria-hidden="true"></span> Tonics</div>
    </header>
    <section class="contact-band">
      <h1 class="person-name">Ulrich Benedetti</h1>
      <ul class="contact-list">
        <li class="contact-phone">Telephone: 800-417-9368</li>
        <li class="contact-email">E-Mail: Ulrich@MabelsTonics.example</li>
        <li class="contact-web">www.MabelsTonics.example</li>
      </ul>
    </section>
  </main>
</body>
</html>
```